Corvale Real Estate

I manage 2 firms. The first one is Felmont and the logo is in blue (see the file) but i need a design for my business card for the second firm called CORVALE IMMOBILIER. This one is in charge of Real estate developer.

Colors
3176b5

```html
<!DOCTYPE html>
<html lang="en">
<head>
<meta charset="utf-8">
<title>Corvale Immobilier – Business Card</title>
<link href="https://fonts.googleapis.com/css2?family=Lato:wght@400;700;900&display=swap" rel="stylesheet">
<style>
  :root {
    --bg: #1c1c1e;
    --card: #111113;
    --brand-blue: #3176b5;
    --text-light: #e6e6e6;
    --text-grey: #bdbdbd;
    --rule: #4a4a4e;
  }
  * { box-sizing: border-box; margin: 0; padding: 0; }
  html, body {
    width: 1200px; height: 900px; overflow: hidden;
    background: var(--bg);
    font-family: "Lato", sans-serif;
  }
  .canvas { position: relative; width: 1200px; height: 900px; }
  .card {
    position: absolute; width: 560px; height: 320px;
    background: var(--card); border-radius: 22px;
    box-shadow: 0 18px 40px rgba(0,0,0,.55);
  }
  .card--back { left: 110px; top: 110px; }
  .card--front { left: 530px; top: 470px; }

  /* Back side */
  .back-mark {
    position: absolute; left: 0; right: 0; top: 105px;
    display: flex; align-items: center; justify-content: center; gap: 14px;
  }
  .back-mark__square { width: 18px; height: 18px; background: var(--text-light); }
  .back-mark__name {
    color: var(--text-light); font-weight: 900; font-size: 34px; letter-spacing: 2px;
  }
  .back-url {
    position: absolute; left: 0; right: 0; top: 232px; text-align: center;
    color: var(--text-light); font-weight: 700; font-size: 15px; letter-spacing: .3px;
  }

  /* Front side */
  .brand {
    position: absolute; right: 36px; top: 38px;
    display: flex; align-items: center; gap: 14px;
  }
  .brand__square { width: 22px; height: 22px; background: var(--brand-blue); }
  .brand__name {
    color: var(--brand-blue); font-weight: 900; font-size: 30px;
    line-height: 1; letter-spacing: 1px;
  }
  .rule {
    position: absolute; left: 250px; right: 36px; top: 140px;
    height: 1px; background: var(--rule);
  }
  .person { position: absolute; left: 40px; top: 118px; }
  .person__name {
    color: var(--brand-blue); font-size: 22px; font-weight: 400; letter-spacing: .5px;
  }
  .person__title { color: var(--text-light); font-size: 15px; margin-top: 2px; }
  .address {
    position: absolute; right: 36px; top: 158px; text-align: right;
    color: var(--text-light); font-size: 15px; line-height: 1.4;
  }
  .contacts {
    position: absolute; left: 40px; top: 212px; list-style: none;
    color: var(--text-light); font-size: 15px; line-height: 1.45;
  }
  .contacts li { display: flex; align-items: center; gap: 9px; }
  .contacts svg { width: 13px; height: 13px; fill: var(--brand-blue); flex: none; }
</style>
</head>
<body>
<main class="canvas">
  <section class="card card--back" aria-label="Card back">
    <div class="back-mark">
      <span class="back-mark__square"></span>
      <span class="back-mark__name">CORVALE</span>
    </div>
    <p class="back-url">www.corvale-immo.com</p>
  </section>

  <section class="card card--front" aria-label="Card front">
    <div class="brand">
      <span class="brand__square"></span>
      <span class="brand__name">CORVALE IMMOBILIER</span>
    </div>
    <div class="rule"></div>
    <div class="person">
      <p class="person__name">MARCUS DELORME</p>
      <p class="person__title">Managing Director</p>
    </div>
    <address class="address" style="font-style:normal">
      18, Rue des Tilleuls<br>Lyon, France 69003
    </address>
    <ul class="contacts">
      <li>
        <svg viewBox="0 0 16 16"><path d="M3.6 1.2l2.3 2.6-1.3 1.8c.9 2 2.6 3.7 4.6 4.6l1.8-1.3 2.6 2.3-1.2 2.4C7.4 15.3.7 8.6 1.2 3.4z"/></svg>
        044-987 654 321
      </li>
      <li>
        <svg viewBox="0 0 16 16"><path d="M1 3h14v1.2L8 9 1 4.2z"/><path d="M1 5.6l7 4.8 7-4.8V13H1z"/></svg>
        info@corvale-immo.com
      </li>
      <li>
        <svg viewBox="0 0 16 16"><circle cx="8" cy="8" r="7"/></svg>
        www.corvale-immo.com
      </li>
    </ul>
  </section>
</main>
</body>
</html>
```